Accounting firm needing business card / letterhead designed
Marcus T. Elbering, CPA
marcus@fernquill.com
www.fernquill.com
482 N Harlow Ave Larkfield, NV 43719
775-555-0172

```html
<!DOCTYPE html>
<html lang="en">
<head>
<meta charset="utf-8">
<title>Fernquill Solutions – Business Card</title>
<link href="https://fonts.googleapis.com/css2?family=Open+Sans:wght@400;600&display=swap" rel="stylesheet">
<style>
  :root {
    --backdrop: #3b3d3c;
    --card: #ffffff;
    --navy: #2a2868;
    --green: #7cc242;
    --band: #062823;
    --ink: #111a18;
    --rule: #4d5a57;
  }
  * { box-sizing: border-box; margin: 0; padding: 0; }
  html, body {
    width: 1200px; height: 900px; overflow: hidden;
    background: var(--backdrop);
    font-family: "Open Sans", sans-serif;
  }
  .stage {
    position: relative; width: 1200px; height: 900px;
    display: flex; flex-direction: column; align-items: center; justify-content: center; gap: 50px;
  }
  .card {
    position: relative; width: 630px; height: 360px;
    background: var(--card);
    box-shadow: 0 6px 18px rgba(0,0,0,.35);
    overflow: hidden;
  }
  /* brand lockup */
  .brand { display: flex; align-items: center; gap: 14px; }
  .brand-mark { width: 18px; height: 18px; background: var(--navy); flex: none; }
  .brand-name {
    color: var(--navy); font-weight: 600; letter-spacing: .12em; text-transform: uppercase; white-space: nowrap;
  }
  /* back */
  .card-back { display: flex; flex-direction: column; align-items: center; justify-content: center; gap: 34px; }
  .card-back .brand-name { font-size: 34px; }
  .website { font-size: 21px; font-weight: 600; letter-spacing: .16em; color: var(--ink); }
  /* front */
  .band-top { position: absolute; left: 0; top: 0; width: 100%; height: 14px; background: var(--band); }
  .band-bottom { position: absolute; left: 0; top: 292px; width: 100%; height: 40px; background: var(--band); }
  .card-front .brand { position: absolute; left: 34px; top: 42px; }
  .card-front .brand-name { font-size: 21px; }
  .card-front .brand-mark { width: 14px; height: 14px; }
  .holder { position: absolute; right: 40px; top: 94px; width: 300px; text-align: center; color: var(--ink); }
  .holder-name { font-size: 24px; font-weight: 600; letter-spacing: .1em; line-height: 1.3; }
  .holder-rule { height: 1px; background: var(--rule); margin: 6px 0 4px; }
  .holder-title { font-size: 17px; font-weight: 600; letter-spacing: .1em; line-height: 1.3; }
  .contacts { position: absolute; left: 188px; top: 182px; list-style: none; }
  .contacts li { display: flex; align-items: center; gap: 14px; height: 34px; font-size: 15px; letter-spacing: .1em; color: var(--ink); white-space: nowrap; }
  .contacts svg { width: 22px; height: 22px; flex: none; }
</style>
</head>
<body>
<main class="stage">
  <section class="card card-back">
    <div class="brand"><span class="brand-mark"></span><span class="brand-name">Fernquill Solutions</span></div>
    <p class="website">www.fernquill.com</p>
  </section>

  <section class="card card-front">
    <div class="band-top"></div>
    <div class="brand"><span class="brand-mark"></span><span class="brand-name">Fernquill Solutions</span></div>
    <div class="holder">
      <p class="holder-name">Marcus T. Elbering</p>
      <div class="holder-rule"></div>
      <p class="holder-title">CPA</p>
    </div>
    <ul class="contacts">
      <li>
        <svg viewBox="0 0 24 24" aria-hidden="true"><circle cx="12" cy="12" r="10.5" fill="none" stroke="#111a18" stroke-width="1.6"/><rect x="6.5" y="8" width="11" height="8" fill="none" stroke="#111a18" stroke-width="1.4"/><path d="M6.5 8 12 12.5 17.5 8" fill="none" stroke="#111a18" stroke-width="1.4"/></svg>
        marcus@fernquill.com
      </li>
      <li>
        <svg viewBox="0 0 24 24" aria-hidden="true"><circle cx="12" cy="12" r="10.5" fill="none" stroke="#111a18" stroke-width="1.6"/><path d="M12 18.5c-3-3.6-4.5-6-4.5-8a4.5 4.5 0 0 1 9 0c0 2-1.5 4.4-4.5 8z" fill="#111a18"/><circle cx="12" cy="10.3" r="1.6" fill="#fff"/></svg>
        482 N Harlow Ave Larkfield, NV 43719
      </li>
      <li>
        <svg viewBox="0 0 24 24" aria-hidden="true"><circle cx="12" cy="12" r="10.5" fill="none" stroke="#111a18" stroke-width="1.6"/><path d="M9 6.5h2l1 3-1.5 1c.6 1.4 1.6 2.4 3 3l1-1.5 3 1v2c0 .8-.7 1.5-1.5 1.5C11 16.5 7.5 13 7.5 8 7.5 7.2 8.2 6.5 9 6.5z" fill="#111a18"/></svg>
        775-555-0172
      </li>
    </ul>
    <div class="band-bottom"></div>
  </section>
</main>
</body>
</html>
```